complete redesign of VitaPlate.com

VITAPLATE.COM
MAIN MANU

We need it cut into HTML / Wordpress Friendly.... Our developer will handle all the WP / PHP coding, but we need it placed into HTML format so he can put into wordpress.

Please see the old vitaplate.com by visiting www.vitaplate.com... we want something completely different, but... just use this site for reference as to audience, theme, etc... we want something where it is science meets diet in helping fight cancer :)

WE NEED SOMETHING MORE MODERN AND MEDICAL IN TERMS OF DESIGN

See below:

1 CANCER NEWS
2 NUTRITION DIAGNOSTICS
3 DIET STEPS
4 DIET SUPPLEMENTS IN CANCER 
5 DICTIONARY OF MARKINGS ON FOOD
6 MERIVOLA VIDEOS
7 YOUR INDIVIDUAL DIET - SUBSCRIPTION

a. CANCER NEWS - latest articles relating to cancer prevention research treatments

b. NUTRITION DIAGNOSTICS -  description of the research that must be done to determine the degree of malnutrition of the body a place on the charts
pictures, etc.

c. DIET STEPS 
(sub menu - @)
¥ prevention of oncological - @
¥ diet chemotherapy - @
¥ diet in radiotherapy - @
¥ hormonal diet - @
¥ diet during convalescence - @

d. DIET SUPPLEMENTS IN CANCER - articles describing various supplements summary tables, etc.

e. DICTIONARY OF MARKINGS ON FOOD - composition, translation of labels on food, itd.

f. MERIVOLA VIDEOS 
(sub menu - @)
¥ healthy cooking - @
¥ meal preparation - @
¥ storage of food - @
¥ eco food - @
¥ rehabilitation - @
¥ yoga - @
¥ exercises - @
¥ psycho-oncology training - @
¥ music therapy - @

g. YOUR INDIVIDUAL DIET -  individual personalized diet for subscribing. We
add this point by developing a system of diet.

After 3 months, we will add special individual programs that mix diet, exercise and psychological lectures

Industry/Entity Type

Medical

Logo Text

Vita Plate / VitaPlate.com

Number of Pages Required

5+ page

Font styles to use
Sans Serif

Colors
ec1f27
9bcb3c
ffffff

Requirements
Must have
• HTML/CSS

```html
<!DOCTYPE html>
<html lang="en">
<head>
<meta charset="utf-8">
<title>Vita Plate</title>
<link href="https://fonts.googleapis.com/css2?family=Oswald:wght@300;400;500&family=Roboto:wght@300;400;500;700&display=swap" rel="stylesheet">
<style>
:root{
  --green:#8dc63f;
  --green-dark:#7db334;
  --red:#ec1f27;
  --ink:#222;
  --text:#666;
  --muted:#999;
  --line:#d5d5d5;
  --panel:#3a3a3a;
  --panel-dark:#2e2e2e;
  --white:#fff;
}
*{box-sizing:border-box;margin:0;padding:0}
html,body{width:1200px;height:2980px;overflow:hidden;background:var(--white);font-family:'Roboto',Arial,sans-serif;color:var(--text)}
.page{position:relative;width:1200px;height:2980px}

/* header */
.site-header{position:absolute;left:0;top:0;width:1200px;height:90px;background:var(--white);border-bottom:2px solid var(--green)}
.brand{position:absolute;left:56px;top:24px;display:flex;align-items:center;gap:12px}
.brand-dot{width:42px;height:42px;border-radius:50%;background:var(--red)}
.brand-name{font-family:'Oswald',sans-serif;font-weight:500;font-size:24px;color:var(--ink);letter-spacing:.5px}
.main-nav a{position:absolute;top:0;height:88px;line-height:88px;font-family:'Oswald',sans-serif;font-weight:300;font-size:17px;color:#333;text-decoration:none;text-transform:uppercase}
.main-nav a.active{background:var(--green);color:var(--white);padding:0 14px;left:290px;width:64px}

/* hero */
.hero{position:absolute;left:0;top:90px;width:1200px;height:530px;background:linear-gradient(100deg,#b9bcbf 0%,#e4e6e8 35%,#cfd2d4 60%,#f1f2f2 100%)}
.hero-title{position:absolute;left:152px;top:176px;width:342px;height:54px;background:var(--green);color:var(--white);font-family:'Oswald',sans-serif;font-weight:300;font-size:28px;line-height:54px;padding-left:22px}
.hero-sub{position:absolute;left:152px;top:240px;background:rgba(255,255,255,.85);font-size:14px;color:#444;padding:6px 16px}
.hero-btn{position:absolute;left:152px;top:298px;width:158px;height:40px;background:var(--green);color:var(--white);font-family:'Oswald',sans-serif;font-weight:300;font-size:18px;line-height:40px;text-align:center}

/* booking form */
.field{position:absolute;height:22px;border-bottom:1px solid var(--line);font-size:10px;color:var(--muted);padding-left:22px;letter-spacing:.5px}
.book-btn{position:absolute;left:820px;top:698px;width:140px;height:34px;background:var(--green);color:var(--white);font-size:11px;font-weight:500;text-align:center;line-height:34px}

/* call band */
.call-band{position:absolute;left:58px;top:768px;width:1088px;height:62px;background:linear-gradient(90deg,#e6e6e6,#f4f4f4 60%,#e0e0e0)}
.call-photo{position:absolute;left:0;top:0;width:82px;height:62px;background:linear-gradient(135deg,#9aa0a4,#d7d9db)}
.call-box{position:absolute;left:82px;top:0;width:346px;height:62px;background:var(--green);color:var(--white)}
.call-label{position:absolute;left:24px;top:15px;font-size:12px;font-weight:500;line-height:16px}
.call-sep{position:absolute;left:150px;top:14px;width:1px;height:34px;background:rgba(255,255,255,.7)}
.call-number{position:absolute;left:172px;top:14px;font-family:'Oswald',sans-serif;font-size:24px;font-weight:400;line-height:34px}

/* section heads */
.kicker{position:absolute;left:0;width:1200px;text-align:center;font-size:10px;letter-spacing:1px;color:#aaa}
.section-title{position:absolute;left:0;width:1200px;text-align:center;font-size:22px;font-weight:500;color:var(--ink);letter-spacing:.5px}

/* services */
.service{position:absolute;width:320px}
.service svg{position:absolute;left:0;top:0}
.service h3{position:absolute;left:50px;top:0;font-size:15px;font-weight:500;color:var(--ink)}
.service p{position:absolute;left:50px;top:26px;width:240px;font-size:11px;line-height:17px;color:#888}

/* videos */
.vids{position:absolute;left:58px;top:1270px;width:1088px;height:476px;background:linear-gradient(120deg,#2f3436 0%,#4a4d4f 50%,#3d4042 100%)}
.vids-kicker{position:absolute;left:64px;top:58px;font-size:11px;color:#ddd}
.vids-title{position:absolute;left:64px;top:74px;font-family:'Oswald',sans-serif;font-weight:400;font-size:34px;color:var(--white)}
.vids-rule{position:absolute;left:64px;top:120px;width:250px;height:1px;background:#bbb}
.vid{position:absolute;width:500px;height:124px}
.vid-thumb{position:absolute;left:0;top:0;width:158px;height:124px}
.vid h4{position:absolute;left:178px;top:4px;width:250px;font-size:14px;font-weight:700;color:var(--white);line-height:20px}
.vid .meta{position:absolute;left:178px;top:50px;font-size:10px;color:#ddd}
.vid p{position:absolute;left:178px;top:76px;width:320px;font-size:10px;line-height:20px;color:var(--white)}

/* tabs */
.tab-heading{position:absolute;left:0;width:1200px;top:1814px;text-align:center;font-size:22px;color:var(--ink);font-weight:400;letter-spacing:.5px}
.tab-heading span{margin:0 20px;color:#555}
.tab-menu{position:absolute;left:58px;top:1900px;width:252px}
.tab-menu li{list-style:none;height:38px;line-height:44px;font-size:12px;font-weight:500;color:var(--ink);padding-left:12px}
.tab-menu li.active{background:#efefef;height:44px;margin-bottom:8px}
.tab-photo{position:absolute;left:336px;top:1896px;width:810px;height:298px;background:linear-gradient(135deg,#c0733a 0%,#e9e3dc 35%,#f5f2ee 60%,#d07a3a 85%,#8c4a28 100%)}
.article{position:absolute;left:336px;top:2194px;width:810px;height:400px;border-left:1px solid #eee}
.article h2{position:absolute;left:40px;top:40px;font-size:44px;font-weight:500;color:#111}
.article p{position:absolute;left:40px;width:740px;font-size:12px;line-height:28px;color:#888}
.read-more{position:absolute;left:42px;top:340px;font-size:12px;color:var(--ink);border-bottom:1px solid #ccc;padding-bottom:4px}

/* footer */
.site-footer{position:absolute;left:58px;top:2660px;width:1088px;height:280px;background:var(--panel)}
.footer-col{position:absolute;top:0;height:280px}
.footer-col h5{position:absolute;top:50px;font-size:12px;font-weight:700;color:var(--white);white-space:nowrap}
.footer-col .txt{font-size:12px;line-height:26px;color:#aaa}
.footer-divider{position:absolute;top:42px;width:1px;height:200px;background:#555}
.newsletter{position:absolute;left:66px;top:142px;width:276px;border-bottom:2px solid var(--white);font-size:12px;color:#ccc;padding-bottom:6px}
.subscribe{position:absolute;left:66px;top:200px;width:276px;height:40px;background:var(--green);color:var(--white);font-size:12px;text-align:center;line-height:40px}
.social{position:absolute;top:170px;width:36px;height:36px;border:2px solid var(--white);border-radius:50%}
.copyright{position:absolute;left:58px;top:2940px;width:1088px;height:40px;background:var(--panel-dark);text-align:center;line-height:40px;font-size:12px;color:#999}
</style>
</head>
<body>
<div class="page">

<header class="site-header">
  <div class="brand"><span class="brand-dot"></span><span class="brand-name">VITA PLATE</span></div>
  <nav class="main-nav">
    <a class="active" href="#">Home</a>
    <a href="#" style="left:372px">News</a>
    <a href="#" style="left:440px">Nutrition</a>
    <a href="#" style="left:536px">Diet Steps</a>
    <a href="#" style="left:640px">Diet Supplements in Cancer</a>
    <a href="#" style="left:862px">Dictionary</a>
    <a href="#" style="left:972px">Videos</a>
    <a href="#" style="left:1052px">Subscription</a>
  </nav>
</header>

<section class="hero" role="img" aria-label="Laboratory scene with a gloved hand holding a test tube">
  <div class="hero-title">YOU ARE WHAT YOU EAT</div>
  <div class="hero-sub">Lorem ipsum dolor sit amet, consectetuer adipiscing elit</div>
  <div class="hero-btn">VIEW DETAILS</div>
</section>

<form class="booking">
  <div class="field" style="left:140px;top:658px;width:254px">YOUR FULL NAME</div>
  <div class="field" style="left:430px;top:658px;width:252px">YOUR EMAIL ADDRESS</div>
  <div class="field" style="left:708px;top:658px;width:252px">YOUR PHONE NUMBER</div>
  <div class="field" style="left:140px;top:704px;width:254px">APPOINTMENT DATE</div>
  <div class="field" style="left:430px;top:704px;width:252px">YOUR MESSAGE</div>
  <div class="book-btn">BOOK NOW</div>
</form>

<div class="call-band">
  <div class="call-photo" role="img" aria-label="Laboratory equipment"></div>
  <div class="call-box">
    <div class="call-label">BOOK THROUGH<br>CALL NOW</div>
    <div class="call-sep"></div>
    <div class="call-number">123 4860 217</div>
  </div>
</div>

<div class="kicker" style="top:876px">GET WELL SOON</div>
<h2 class="section-title" style="top:896px">ORVANTHE SERVICES</h2>

<section class="services">
  <div class="service" style="left:60px;top:1002px">
    <svg width="32" height="24" viewBox="0 0 32 24" fill="none" stroke="#8dc63f" stroke-width="2.5"><path d="M2 4v18M2 16h28v6M2 12h28M8 8h6"/></svg>
    <h3>Emergency Care</h3>
    <p>Lorem ipsum dolor sit amet, consectetur adipiscing elit. Cum consectetur sit ullam perspiciatis, deserunt.</p>
  </div>
  <div class="service" style="left:430px;top:1002px">
    <svg width="30" height="28" viewBox="0 0 30 28" fill="none" stroke="#8dc63f" stroke-width="2.5"><path d="M15 2v24M3 6c4 0 8 2 12 6 4-4 8-6 12-6M8 14c3 0 5 2 7 4 2-2 4-4 7-4"/></svg>
    <h3>Operation Thearer</h3>
    <p>Lorem ipsum dolor sit amet, consectetur adipiscing elit. Cum consectetur sit ullam perspiciatis, deserunt.</p>
  </div>
  <div class="service" style="left:806px;top:1002px">
    <svg width="30" height="30" viewBox="0 0 30 30" fill="none" stroke="#8dc63f" stroke-width="2.5"><path d="M5 3v8a6 6 0 0 0 12 0V3M11 17v5a5 5 0 0 0 10 0v-4"/><circle cx="21" cy="14" r="3"/></svg>
    <h3>Outdoor Checkup</h3>
    <p>Lorem ipsum dolor sit amet, consectetur adipiscing elit. Cum consectetur sit ullam perspiciatis, deserunt.</p>
  </div>
  <div class="service" style="left:60px;top:1132px">
    <svg width="30" height="32" viewBox="0 0 30 32" fill="none" stroke="#8dc63f" stroke-width="2.5"><path d="M10 2h6M13 2v18M6 30h18M13 20c-4 0-6 3-6 6h12M20 10c3 2 5 6 3 10"/></svg>
    <h3>Cancer Service</h3>
    <p>Lorem ipsum dolor sit amet, consectetur adipiscing elit. Cum consectetur sit ullam perspiciatis, deserunt.</p>
  </div>
  <div class="service" style="left:430px;top:1132px">
    <svg width="32" height="28" viewBox="0 0 32 28"><path d="M16 27 3 14A7.5 7.5 0 0 1 16 5a7.5 7.5 0 0 1 13 9z" fill="#8dc63f"/><path d="M5 14h7l2-4 3 8 2-4h8" fill="none" stroke="#fff" stroke-width="2"/></svg>
    <h3>Blood Test</h3>
    <p>Lorem ipsum dolor sit amet, consectetur adipiscing elit. Cum consectetur sit ullam perspiciatis, deserunt.</p>
  </div>
  <div class="service" style="left:806px;top:1132px">
    <svg width="30" height="30" viewBox="0 0 30 30" fill="#8dc63f"><circle cx="19" cy="9" r="7"/><rect x="2" y="14" width="18" height="10" rx="5" transform="rotate(-35 11 19)"/></svg>
    <h3>Pharmacy</h3>
    <p>Lorem ipsum dolor sit amet, consectetur adipiscing elit. Cum consectetur sit ullam perspiciatis, deserunt.</p>
  </div>
</section>

<section class="vids" role="img" aria-label="Dark background photo of a stethoscope on a medical chart">
  <div class="vids-kicker">RECENT POSTS</div>
  <h2 class="vids-title">NEWEST VIDS</h2>
  <div class="vids-rule"></div>

  <article class="vid" style="left:64px;top:136px">
    <div class="vid-thumb" role="img" aria-label="Jars of herbs and spices" style="background:linear-gradient(135deg,#6d8a4a,#e8e6da 60%,#4f6b33)"></div>
    <h4>DIFFERENT TYPES OF STROKE ADIPISICING AMET</h4>
    <div class="meta">August 8, 2015 | Lena Marsk</div>
    <p>Lorem ipsum dolor adipisicing amet, consectetur<br>Aspernatur incididnt quo officia</p>
  </article>
  <article class="vid" style="left:556px;top:136px">
    <div class="vid-thumb" role="img" aria-label="Bowl of dried chili flakes" style="background:linear-gradient(135deg,#7a3a1e,#c8642e 50%,#e7d8c6)"></div>
    <h4>DIFFERENT TYPES OF STROKE ADIPISICING AMET</h4>
    <div class="meta">August 8, 2015 | Lena Marsk</div>
    <p>Lorem ipsum dolor adipisicing amet, consectetur sit elit.<br>Aspernatur incididnt quo officia</p>
  </article>
  <article class="vid" style="left:64px;top:296px">
    <div class="vid-thumb" role="img" aria-label="Plate of pasta with seasoning" style="background:linear-gradient(135deg,#5a4a3a,#f2ece2 50%,#c79a5a)"></div>
    <h4>DIFFERENT TYPES OF STROKE ADIPISICING AMET</h4>
    <div class="meta">August 8, 2015 | Lena Marsk</div>
    <p>Lorem ipsum dolor adipisicing amet, consectetur<br>Aspernatur incididnt quo officia</p>
  </article>
  <article class="vid" style="left:556px;top:296px">
    <div class="vid-thumb" role="img" aria-label="Wooden spoons with whole spices" style="background:linear-gradient(135deg,#2a1c14,#6e4328 50%,#3a2618)"></div>
    <h4>DIFFERENT TYPES OF STROKE ADIPISICING AMET</h4>
    <div class="meta">August 8, 2015 | Lena Marsk</div>
    <p>Lorem ipsum dolor adipisicing amet, consectetur sit elit.<br>Aspernatur incididnt quo officia</p>
  </article>
</section>

<div class="kicker" style="top:1798px">GET WELL SOON</div>
<h2 class="tab-heading">VITA PLATE<span>|</span>RECIPES<span>|</span>SUCCESS STORIES</h2>

<ul class="tab-menu">
  <li class="active">OVERVIEW</li>
  <li>THE DIFFERENCE</li>
  <li>BENEFITS</li>
</ul>
<div class="tab-photo" role="img" aria-label="Jars and white bowls of ground spices and cloves"></div>
<article class="article">
  <h2>Hello!</h2>
  <p style="top:120px">Halden Company is the leading resource for custom-engineered metal building systems of the highest quality, making us one of the most trusted names in the industry and a builder's first choice when their projects matter most.<br>When you partner with us, you're getting invaluable technical assistance and hands-on support—so the entire process is easier from start to finish.</p>
  <p style="top:264px">"Halden Building delivers quality products combined with outstanding service. We are committed to revitalizing our domestic and international partnerships—with a passion for quality and restoring customer dedication."</p>
  <div class="read-more">READ MORE ......</div>
</article>

<footer class="site-footer">
  <div class="footer-col" style="left:66px;width:290px">
    <h5>STAY FRIENDS WITH US</h5>
    <div class="txt" style="position:absolute;top:76px;width:290px;line-height:20px;font-size:12px">Subscribe to our newsletter and stay updated with the latest news.</div>
  </div>
  <div class="newsletter">NEWSLETTER</div>
  <div class="subscribe">SUBSCRIBE</div>
  <div class="footer-divider" style="left:406px"></div>
  <div class="footer-col" style="left:466px;width:200px">
    <h5>CATEGORIES</h5>
    <div class="txt" style="position:absolute;top:82px">VIDEO RECIPES<br>SCIENTIFIC APPROACH<br>OUR TEAM<br>BLOG</div>
  </div>
  <div class="footer-divider" style="left:676px"></div>
  <div class="footer-col" style="left:744px;width:320px">
    <h5>FOLLOW/CONNECT</h5>
    <div class="txt" style="position:absolute;top:80px;line-height:20px;white-space:nowrap">Choosing a doctorTake proper treatment<br>Discuss your doctorFind medical error<br>Report progress condition<br>Primary medical care</div>
  </div>
  <div class="social" style="left:746px"></div>
  <div class="social" style="left:792px"></div>
  <div class="social" style="left:838px"></div>
  <div class="social" style="left:884px"></div>
</footer>
<div class="copyright">© 2015 by Vita Plate</div>

</div>
</body>
</html>
```